Criação de Papelaria Profissional para Beleza
" CLÍNICA DE ESTÉTICA COMPLETA, COM ÊNFASE EM ATENDIMENTO PRÊMIUM (salas exclusivas, máquinas próprias, ambiente aconchegante com forte conexão nordestina) Serviços ofertados: Estética corporal, facial, injetáveis e laser) SITE: https://brunelva.com.br/ "

```html
<!DOCTYPE html>
<html lang="pt-BR">
<head>
<meta charset="UTF-8">
<title>Brunelva – Cartão Fidelidade</title>
<link rel="stylesheet" href="https://fonts.googleapis.com/css2?family=Tenor+Sans&family=Montserrat:wght@400;600;700&display=swap">
<style>
  :root {
    --rose: #c27d70;
    --rose-deep: #a9695d;
    --cream: #f4ece7;
    --blush: #f7e9e4;
    --white: #ffffff;
    --backdrop: #e9e4e1;
  }
  * { margin: 0; padding: 0; box-sizing: border-box; }
  html, body { width: 1200px; height: 1200px; overflow: hidden; }
  body {
    background: var(--backdrop);
    font-family: "Montserrat", sans-serif;
    position: relative;
  }
  .card {
    position: absolute;
    left: 180px;
    width: 840px;
    height: 480px;
    border-radius: 6px;
    box-shadow: 0 10px 30px rgba(80, 50, 40, 0.12);
    overflow: hidden;
  }
  /* Front */
  .card-front { top: 90px; background: var(--cream); color: var(--rose); }
  .card-front .label {
    position: absolute; left: 44px; top: 40px;
    font-family: "Tenor Sans", sans-serif;
    font-size: 17px; letter-spacing: 3px; line-height: 1.4;
  }
  .brand-lockup {
    position: absolute; left: 0; right: 0; top: 120px;
    display: flex; flex-direction: column; align-items: center;
  }
  .brand-dot {
    width: 110px; height: 110px; border-radius: 50%;
    background: var(--rose);
  }
  .brand-name {
    margin-top: 34px;
    font-family: "Tenor Sans", sans-serif;
    font-size: 64px; letter-spacing: 14px; padding-left: 14px;
    color: var(--rose);
  }
  .brand-tagline {
    margin-top: 10px;
    font-family: "Tenor Sans", sans-serif;
    font-size: 17px; letter-spacing: 6px; padding-left: 6px;
  }
  /* Back */
  .card-back { top: 630px; background: var(--rose); color: var(--white); }
  .offer {
    position: absolute; left: 0; right: 0; top: 38px;
    text-align: center; font-size: 17px; letter-spacing: 1.5px; line-height: 1.45;
  }
  .offer strong { font-weight: 700; }
  .stamps {
    position: absolute; left: 85px; top: 110px;
    display: grid; grid-template-columns: repeat(5, 110px); gap: 24px 30px;
  }
  .stamp {
    width: 110px; height: 110px; border-radius: 50%;
    background: var(--blush);
  }
  .contacts {
    position: absolute; left: 85px; right: 60px; top: 385px;
    display: grid; grid-template-columns: 1fr 1.3fr; gap: 10px 30px;
    font-size: 14px; letter-spacing: 0.5px;
  }
  .contact { display: flex; align-items: center; gap: 10px; }
  .contact svg { flex: none; }
  .contact .social-dot { width: 16px; height: 16px; border-radius: 50%; border: 2px solid var(--white); flex: none; }
  .contact.address { align-items: flex-start; line-height: 1.35; }
</style>
</head>
<body>
  <section class="card card-front">
    <p class="label">CARTÃO<br>FIDELIDADE</p>
    <div class="brand-lockup">
      <div class="brand-dot"></div>
      <h1 class="brand-name">BRUNELVA</h1>
      <p class="brand-tagline">CLÍNICA DE ESTÉTICA</p>
    </div>
  </section>

  <section class="card card-back">
    <p class="offer"><strong>APÓS 10 PROCEDIMENTOS</strong> GANHE 01<br>SERVIÇO GRATUITO DE SUA PREFERÊNCIA</p>
    <div class="stamps">
      <div class="stamp"></div><div class="stamp"></div><div class="stamp"></div><div class="stamp"></div><div class="stamp"></div>
      <div class="stamp"></div><div class="stamp"></div><div class="stamp"></div><div class="stamp"></div><div class="stamp"></div>
    </div>
    <div class="contacts">
      <div class="contact">
        <svg width="16" height="16" viewBox="0 0 24 24" fill="none" stroke="#fff" stroke-width="2"><path d="M5 3h4l2 5-2.5 1.5a11 11 0 0 0 6 6L16 13l5 2v4a2 2 0 0 1-2 2A16 16 0 0 1 3 5a2 2 0 0 1 2-2z"/></svg>
        <span>(82) 90412-3870</span>
      </div>
      <div class="contact">
        <svg width="16" height="16" viewBox="0 0 24 24" fill="none" stroke="#fff" stroke-width="2"><circle cx="12" cy="12" r="9"/><path d="M3 12h18M12 3c3 3 3 15 0 18M12 3c-3 3-3 15 0 18"/></svg>
        <span>brunelva.com.br</span>
      </div>
      <div class="contact">
        <span class="social-dot"></span>
        <span>@brunelva.clinica</span>
      </div>
      <div class="contact address">
        <svg width="16" height="18" viewBox="0 0 24 26" fill="none" stroke="#fff" stroke-width="2"><path d="M12 24s8-8 8-14a8 8 0 0 0-16 0c0 6 8 14 8 14z"/><circle cx="12" cy="10" r="3"/></svg>
        <span>Rua das Palmeiras, 120, Centro<br>Maceió - AL</span>
      </div>
    </div>
  </section>
</body>
</html>
```